An Australian based fintech company need a 12 page booklet

We need the booklet to be designed per the content attached. Can refer to a market leader for some design style inspiration - https://solvarin.com.au
Updates
I understand the briefing is somewhat confusing. I will update and extend deadline shortly. Pls pause current the design work thanks.
Need extra days to review
Please add a page prior to the Funding Option page:
How Tarudo Works:
1. Obtain a Quote
Connect with our network of reliable tradespeople to receive quotes, or bring in your preferred tradies, and we'll assist in accrediting them with Tarudo.
2. Apply for Green Funding
Apply for partial or full funding based on your quote and budget. Our straightforward, paperless application process ensures a quick turnaround, and you'll receive prompt notifications regarding your application and approval.
3. Green Home Transformation
Once your green funding is approved, coordinate with our accredited tradespeople to schedule the installation.
4. Savings Commence
After confirming the completion of the work, we'll release the full payment to your tradie. Fortnightly repayments will initiate, facilitated through either credit card or direct debit.
Target Market(s)
Australian local household
Industry/Entity Type
Green Fintech
Look and feel
Each slider illustrates characteristics of the customer's brand and the style your logo design should communicate.

```html
<!DOCTYPE html>
<html lang="en">
<head>
<meta charset="utf-8">
<title>Tarudo Booklet Spreads</title>
<link rel="stylesheet" href="https://fonts.googleapis.com/css2?family=Montserrat:wght@500;700;800&family=Open+Sans:wght@400;600&display=swap">
<style>
:root{
  --bg:#ececec;
  --paper:#ffffff;
  --green:#3aaa35;
  --green-dark:#1f7a34;
  --green-light:#8dc63f;
  --green-pale:#e6f3d8;
  --ink:#3c3c3c;
  --muted:#6d6d6d;
}
*{box-sizing:border-box;margin:0;padding:0}
html,body{width:820px;height:1200px;overflow:hidden;background:var(--bg)}
body{position:relative;font-family:"Open Sans",Arial,sans-serif;color:var(--ink)}
.page{position:absolute;width:248px;height:352px;background:var(--paper);overflow:hidden;box-shadow:0 1px 4px rgba(0,0,0,.18)}
.c1{left:16px}.c2{left:286px}.c3{left:556px}
.r1{top:48px}.r2{top:424px}.r3{top:800px}
.deco{position:absolute;inset:0;width:100%;height:100%}
.brand{position:absolute;display:flex;align-items:center;gap:4px;font-family:"Montserrat",Arial,sans-serif;font-weight:800;color:var(--green);letter-spacing:.3px}
.brand .dot{width:8px;height:8px;border-radius:50%;background:var(--green)}
.brand.small{top:12px;right:14px;font-size:9px}
.brand.small .dot{width:6px;height:6px}
.body{font-size:4.6px;line-height:1.55;color:var(--muted)}
.body p{margin-bottom:5px}
.h-sec{font-family:"Montserrat",Arial,sans-serif;font-weight:700;color:var(--green);font-size:6.5px;margin:6px 0 3px}

/* cover */
.cover-photo{position:absolute;left:0;top:0;width:100%;height:200px;background:linear-gradient(160deg,#c7b49a,#8f7a62 60%,#5f7d49)}
.cover .brand{left:0;right:0;top:236px;justify-content:center;font-size:18px}
.cover .brand .dot{width:12px;height:12px}
.tagline{position:absolute;left:0;right:0;top:292px;text-align:center;font-family:"Montserrat",Arial,sans-serif;font-weight:700;font-size:9px;color:var(--green-dark)}

/* about */
.about-title{position:absolute;left:20px;top:30px;font-family:"Montserrat",Arial,sans-serif;font-weight:800;font-size:20px;color:#fff}
.about .brand.small{color:#fff}.about .brand.small .dot{background:#fff}
.checks{position:absolute;left:20px;top:70px;width:190px;list-style:none}
.checks li{display:flex;align-items:center;gap:4px;font-size:5px;color:#fff;margin-bottom:5px}
.checks svg{width:6px;height:6px;flex:none}
.options{position:absolute;left:20px;top:172px;width:200px}
.options h3{font-family:"Montserrat",Arial,sans-serif;font-weight:700;font-size:8px;color:var(--green-dark);margin-bottom:5px}
.options ul{list-style:none;font-size:5px;color:var(--muted)}
.options li{margin-bottom:3px}
.options li::before{content:"";display:inline-block;width:3px;height:3px;border-radius:50%;background:var(--green);margin-right:4px;vertical-align:middle}

/* story */
.story-text{position:absolute;left:132px;top:58px;width:100px}
.story-text h3{font-family:"Montserrat",Arial,sans-serif;font-size:6px;color:var(--green-dark);margin-bottom:4px}

/* why */
.why-title{position:absolute;left:18px;top:38px;font-family:"Montserrat",Arial,sans-serif;font-weight:800;font-size:15px;line-height:1.1;color:var(--green-dark)}
.why-body{position:absolute;left:18px;top:92px;width:200px}
.why-body .lead{font-family:"Montserrat",Arial,sans-serif;font-weight:700;color:var(--green);font-size:5.6px;margin-bottom:5px}

/* benefits */
.benefits{position:absolute;left:18px;top:40px;width:212px}
.benefits .h-sec{font-size:7px;margin-top:10px}

/* options table */
.opt-title{position:absolute;left:18px;top:36px;font-family:"Montserrat",Arial,sans-serif;font-weight:700;font-size:10px;color:var(--green-dark)}
.opt-table{position:absolute;left:18px;top:60px;width:212px;border-collapse:collapse;font-size:5px}
.opt-table th{background:var(--green);color:#fff;text-align:left;font-weight:600;width:70px;padding:0 5px;height:42px;border-bottom:1px solid #fff}
.opt-table td{padding:0 6px;border-bottom:1px solid var(--green-pale);color:var(--muted)}

/* eligibility */
.elig{position:absolute;left:18px;top:40px;width:212px}

/* partners */
.partner{position:absolute;left:18px;top:42px;width:212px}
.band{background:var(--green);color:#fff;font-family:"Montserrat",Arial,sans-serif;font-weight:700;font-size:6px;line-height:1.3;padding:4px 6px;margin:8px 0 4px}

/* closing */
.closing{position:absolute;left:124px;top:60px;width:108px}
.closing h3{font-family:"Montserrat",Arial,sans-serif;font-size:7px;color:var(--green-dark);margin-bottom:4px}
</style>
</head>
<body>

<!-- Cover -->
<section class="page cover c1 r1">
  <div class="cover-photo" role="img" aria-label="Photo of a smiling family at home"></div>
  <svg class="deco" viewBox="0 0 248 352" preserveAspectRatio="none" aria-hidden="true">
    <path d="M0 180 C70 215 150 160 248 190 L248 222 C160 200 80 240 0 214 Z" fill="var(--green)"/>
    <path d="M0 200 C80 232 160 184 248 210 L248 230 C160 214 80 250 0 228 Z" fill="var(--green-light)" opacity=".8"/>
    <path d="M0 352 L0 330 C80 318 170 340 248 322 L248 352 Z" fill="var(--green)"/>
  </svg>
  <div class="brand"><span class="dot"></span>Tarudo</div>
  <p class="tagline">Your Partner in Fuelling<br>Sustainable Living.</p>
</section>

<!-- About -->
<section class="page about c2 r1">
  <svg class="deco" viewBox="0 0 248 352" preserveAspectRatio="none" aria-hidden="true">
    <path d="M0 0 H248 V150 C170 170 80 140 0 165 Z" fill="var(--green)"/>
    <path d="M150 0 H248 V90 C220 60 180 40 150 0 Z" fill="var(--green-light)" opacity=".6"/>
    <path d="M0 352 L0 320 C90 300 170 330 248 300 L248 352 Z" fill="var(--green)"/>
  </svg>
  <div class="brand small"><span class="dot"></span>Tarudo</div>
  <h2 class="about-title">About Us</h2>
  <ul class="checks">
    <li><svg viewBox="0 0 10 10"><path d="M1 5 L4 8 L9 2" stroke="#fff" stroke-width="2" fill="none"/></svg>Fast, paperless green funding approvals</li>
    <li><svg viewBox="0 0 10 10"><path d="M1 5 L4 8 L9 2" stroke="#fff" stroke-width="2" fill="none"/></svg>Flexible fortnightly repayment options</li>
    <li><svg viewBox="0 0 10 10"><path d="M1 5 L4 8 L9 2" stroke="#fff" stroke-width="2" fill="none"/></svg>Accredited tradespeople across Australia</li>
    <li><svg viewBox="0 0 10 10"><path d="M1 5 L4 8 L9 2" stroke="#fff" stroke-width="2" fill="none"/></svg>No hidden fees or surprises</li>
    <li><svg viewBox="0 0 10 10"><path d="M1 5 L4 8 L9 2" stroke="#fff" stroke-width="2" fill="none"/></svg>Funding for solar and batteries</li>
    <li><svg viewBox="0 0 10 10"><path d="M1 5 L4 8 L9 2" stroke="#fff" stroke-width="2" fill="none"/></svg>Support from local specialists</li>
  </ul>
  <div class="options">
    <h3>Our finance options for your sustainable ideas...</h3>
    <p class="body">We offer the following funding for green upgrades:</p>
    <ul>
      <li>Solar panels and inverters</li>
      <li>Home battery storage</li>
      <li>Heat pumps and insulation</li>
      <li>EV chargers at home</li>
    </ul>
  </div>
</section>

<!-- Story -->
<section class="page story c3 r1">
  <svg class="deco" viewBox="0 0 248 352" preserveAspectRatio="none" aria-hidden="true">
    <path d="M0 40 C70 60 110 140 100 352 L0 352 Z" fill="var(--green)"/>
    <path d="M0 120 C50 140 80 220 70 352 L0 352 Z" fill="var(--green-light)" opacity=".7"/>
    <path d="M20 0 C60 20 90 60 110 110" stroke="var(--green-light)" stroke-width="6" fill="none"/>
  </svg>
  <div class="brand small"><span class="dot"></span>Tarudo</div>
  <div class="story-text body">
    <h3>Our Story</h3>
    <p>Tarudo helps Australian households fund solar, batteries and efficient upgrades with clear terms and friendly support from start to finish.</p>
    <p>We work with accredited tradies to make every green project simple, affordable and fast.</p>
  </div>
</section>

<!-- Why partner -->
<section class="page why c1 r2">
  <svg class="deco" viewBox="0 0 248 352" preserveAspectRatio="none" aria-hidden="true">
    <path d="M170 0 H248 V70 C220 40 195 25 170 0 Z" fill="var(--green)"/>
    <path d="M200 0 H248 V40 C230 25 215 15 200 0 Z" fill="var(--green-light)"/>
  </svg>
  <h2 class="why-title">WHY PARTNER<br>WITH US?</h2>
  <div class="why-body body">
    <p>Tarudo is a green fintech built for Australian homes.</p>
    <p class="lead">Add Tarudo's fill-in finance to your payment arsenal to provide your customers with more payment options.</p>
    <p>Our partners gain access to a trusted funding product that helps customers say yes to quality green upgrades without waiting to save up the full amount.</p>
    <p>Quotes convert faster when payment is simple. Customers apply online in minutes and receive a clear decision, so your team can book installations sooner.</p>
    <p>We settle directly with accredited tradies once work is confirmed, keeping your cash flow steady and your paperwork light.</p>
    <p>Join a growing network of installers bringing clean energy to more Australian homes.</p>
  </div>
</section>

<!-- Benefits -->
<section class="page c2 r2">
  <div class="brand small"><span class="dot"></span>Tarudo</div>
  <div class="benefits body">
    <h3 class="h-sec">1. Comprehensive Funding Solutions</h3>
    <p>Fund solar, storage and efficiency projects of many sizes with one simple application and one trusted partner.</p>
    <h3 class="h-sec">2. Flexible Repayment Terms</h3>
    <p>Customers choose fortnightly repayments that suit their budget, with no penalty for paying off early.</p>
    <h3 class="h-sec">3. Streamlined Approval Process</h3>
    <p>Our digital process gives quick decisions and keeps every party informed at each step.</p>
    <h3 class="h-sec">4. Quick Turnaround</h3>
    <p>Once the job is complete, payment is released to the installer without delay.</p>
  </div>
</section>

<!-- Funding options -->
<section class="page c3 r2">
  <div class="brand small"><span class="dot"></span>Tarudo</div>
  <h2 class="opt-title">Tarudo Green Funding Options</h2>
  <table class="opt-table">
    <tr><th>Funding Type</th><td>Green Personal Loan</td></tr>
    <tr><th>Loan Amount</th><td>$2,000 – $50,000</td></tr>
    <tr><th>Term</th><td>2 to 7 years</td></tr>
    <tr><th>Interest Rate</th><td>Fixed, from 6.9% p.a.</td></tr>
    <tr><th>Fees</th><td>Establishment fee applies</td></tr>
    <tr><th>Repayments</th><td>Fortnightly by direct debit</td></tr>
  </table>
</section>

<!-- Eligibility -->
<section class="page c1 r3">
  <svg class="deco" viewBox="0 0 248 352" preserveAspectRatio="none" aria-hidden="true">
    <path d="M0 0 H90 C60 10 30 20 0 40 Z" fill="var(--green-light)"/>
  </svg>
  <div class="elig body">
    <p>To qualify for green funding, applicants should meet the following basic criteria.</p>
    <h3 class="h-sec">1. Home Ownership</h3>
    <p>Applicants should own or be purchasing the property where the green upgrade will be installed.</p>
    <h3 class="h-sec">2. Credit Score</h3>
    <p>A fair credit history helps us offer the best rate and a quick approval.</p>
    <h3 class="h-sec">3. Serviceability</h3>
    <p>We check that repayments fit comfortably within your regular household income and expenses.</p>
  </div>
</section>

<!-- Partner benefits -->
<section class="page c2 r3">
  <svg class="deco" viewBox="0 0 248 352" preserveAspectRatio="none" aria-hidden="true">
    <path d="M0 0 H120 C80 15 40 25 0 30 Z" fill="var(--green-pale)"/>
  </svg>
  <div class="partner body">
    <h3 class="band">Empowering Opportunities: Competitive Rates and Transparent Fee Structure</h3>
    <p>Competitive rates and a clear fee structure help your customers plan with confidence.</p>
    <h3 class="band">Discover the Advantage: Flexible Funding Options to Boost Sales</h3>
    <p>Offer funding at the point of sale and turn more quotes into completed jobs.</p>
    <h3 class="band">Streamlined Operations: Tailored Integration and Payment Solutions</h3>
    <p>Our portal fits your workflow, from quote upload to payment tracking.</p>
    <h3 class="band">Exclusive Perks: Instant Payments for Completed Installations</h3>
    <p>Get paid promptly once the installation is confirmed as complete.</p>
  </div>
</section>

<!-- Closing -->
<section class="page c3 r3">
  <svg class="deco" viewBox="0 0 248 352" preserveAspectRatio="none" aria-hidden="true">
    <path d="M0 0 H40 C100 80 110 220 80 352 H0 Z" fill="var(--green)"/>
    <path d="M0 60 C50 120 60 240 40 352 H0 Z" fill="var(--green-light)" opacity=".7"/>
  </svg>
  <div class="closing body">
    <h3>Get Started</h3>
    <p>Tarudo is committed to making sustainable living affordable for every Australian household.</p>
    <p>Talk to our team today to learn how green funding can support your next project and your customers.</p>
  </div>
</section>

</body>
</html>
```